Pebble Lane real estate investment company needs a poster design

We would like a poster design size 18 x 24.
Poster wording -
I WANT TO BUY YOUR ( finish with logo) logo uploaded
website- www.pebblelane-homes.example
phone # 555-217-8843 ( color red for the phone number)
we would like to see the poster on 2 different backgrounds
Yellow background
White background
horizontal

```html
<!DOCTYPE html>
<html lang="en">
<head>
<meta charset="utf-8">
<title>Pebble Lane — I Want To Buy Your House</title>
<link rel="stylesheet" href="https://fonts.googleapis.com/css2?family=Montserrat:wght@900&family=Arimo:wght@700&display=swap">
<style>
  :root {
    --poster-yellow: #fdc236;
    --ink-black: #000000;
    --paper-white: #ffffff;
    --call-red: #e8202a;
  }
  * { margin: 0; padding: 0; box-sizing: border-box; }
  html, body { width: 1200px; height: 900px; overflow: hidden; }
  body { background: var(--poster-yellow); }
  .poster {
    position: relative;
    width: 1200px;
    height: 900px;
    background: var(--poster-yellow);
  }
  .headline {
    position: absolute;
    top: 72px;
    left: 0;
    width: 100%;
    text-align: center;
    font-family: "Montserrat", sans-serif;
    font-weight: 900;
    font-size: 152px;
    line-height: 135px;
    color: var(--ink-black);
    letter-spacing: -1px;
  }
  .brand {
    position: absolute;
    top: 378px;
    left: 0;
    width: 100%;
    display: flex;
    justify-content: center;
    align-items: center;
    gap: 30px;
  }
  .brand-mark {
    width: 70px;
    height: 70px;
    background: var(--call-red);
  }
  .brand-name {
    font-family: "Montserrat", sans-serif;
    font-weight: 900;
    font-size: 138px;
    line-height: 1;
    color: var(--ink-black);
    letter-spacing: -2px;
  }
  .contact-band {
    position: absolute;
    top: 637px;
    left: 0;
    width: 1200px;
    height: 263px;
    background: var(--ink-black);
    font-family: "Arimo", sans-serif;
    font-weight: 700;
  }
  .contact-line {
    position: absolute;
    left: 0;
    width: 100%;
    display: flex;
    justify-content: center;
    align-items: center;
  }
  .website-line { top: 62px; gap: 18px; }
  .phone-line { top: 140px; gap: 28px; }
  .website {
    color: var(--paper-white);
    font-size: 50px;
    letter-spacing: 0.5px;
  }
  .phone {
    color: var(--call-red);
    font-size: 92px;
    line-height: 1;
  }
  .icon { flex: none; display: block; }
</style>
</head>
<body>
<main class="poster">
  <h1 class="headline">I WANT TO<br>BUY YOUR</h1>

  <div class="brand">
    <span class="brand-mark" aria-hidden="true"></span>
    <span class="brand-name">PEBBLE LANE</span>
  </div>

  <footer class="contact-band">
    <div class="contact-line website-line">
      <svg class="icon" width="74" height="74" viewBox="0 0 74 74" aria-hidden="true">
        <g fill="none" stroke="#fff" stroke-width="5">
          <circle cx="34" cy="34" r="29"/>
          <ellipse cx="34" cy="34" rx="12" ry="29"/>
          <line x1="5" y1="34" x2="63" y2="34"/>
          <line x1="10" y1="19" x2="58" y2="19"/>
          <line x1="10" y1="49" x2="58" y2="49"/>
        </g>
        <path d="M46 42 L72 56 L61 59 L68 71 L63 73 L56 62 L49 70 Z" fill="#fff" stroke="#000" stroke-width="2"/>
      </svg>
      <span class="website">WWW.PEBBLELANE-HOMES.EXAMPLE</span>
    </div>
    <div class="contact-line phone-line">
      <svg class="icon" width="74" height="74" viewBox="0 0 74 74" aria-hidden="true">
        <path d="M14 8 L26 6 L32 22 L24 28 Q30 44 44 52 L50 44 L66 50 L64 62 Q58 70 48 68 Q22 60 8 28 Q6 16 14 8 Z" fill="#fff"/>
        <g fill="none" stroke="#fff" stroke-width="4" stroke-linecap="round">
          <path d="M42 20 Q52 22 54 32"/>
          <path d="M44 10 Q62 14 64 30"/>
        </g>
      </svg>
      <span class="phone">555-217-8843</span>
    </div>
  </footer>
</main>
</body>
</html>
```